PEACFUL ACUPUNCTURE PRACTITIONER NEEDS A NEW COAT

I need a new design for an exiting website http://willowgateneedlework.com/ for a acupuncturist. This will be a minimalism design with lots and lots of white space. Home page and one interior page. Please keep the feeling of calm and peaceful serenity. For Color scheme: https://www.morningfernclinic.com/fertility. The bottom part of the home page with sections and links to the service pages: https://harborlotuswellness.com/. The client likes this the best: http://mfclinic.com/. I'm attaching the logo and content pages.

Target Market(s)

Women

Industry/Entity Type

Wellness, health, wellbeing, meditation

Number of Pages Required

2 page

Font styles to use
Sans Serif
Decorative

Colors

Designer to choose colors to be used in the design.

Requirements
Must have
Nice to have
• Follow new website drafts and links
Should not have
• Busy with bright colors. No poping

```html
<!DOCTYPE html>
<html lang="en">
<head>
<meta charset="utf-8">
<title>Hormone Balance – Willowgate Acupuncture</title>
<link href="https://fonts.googleapis.com/css2?family=Playfair+Display:wght@700&family=Poppins:wght@400;500;600&display=swap" rel="stylesheet">
<style>
:root{
  --accent:#b0747c;
  --accent-soft:#d9b3b7;
  --ink:#4a4a4a;
  --ink-dark:#3b3b3b;
  --line:#e8e8e8;
  --footer:#58575a;
  --footer-text:#e4dfe0;
  --footer-line:#6c6b6e;
  --white:#ffffff;
}
*{margin:0;padding:0;box-sizing:border-box}
html,body{width:668px;height:1200px;overflow:hidden;background:var(--white)}
body{position:relative;font-family:"Poppins",sans-serif;color:var(--ink)}
.abs{position:absolute}

/* header */
.site-header{position:absolute;left:0;top:0;width:668px;height:90px;background:var(--white);box-shadow:0 6px 14px rgba(0,0,0,.04)}
.call-box{left:50px;top:20px;width:18px;height:18px;border:1px solid var(--accent);display:flex;align-items:center;justify-content:center}
.call-text{left:74px;top:20px;line-height:1}
.call-label{font-size:7px;font-weight:500;color:#888;display:block}
.call-number{font-size:8.5px;font-weight:600;color:var(--ink-dark);display:block;margin-top:2px}
.brand{left:0;width:668px;top:20px;display:flex;justify-content:center;align-items:center;gap:7px}
.brand-dot{width:18px;height:18px;border-radius:50%;background:var(--accent-soft)}
.brand-name{font-size:17px;font-weight:400;color:var(--ink)}
.shop-button{left:553px;top:19px;width:66px;height:19px;border:1px solid var(--accent);color:var(--accent);font-size:6.5px;font-weight:600;display:flex;align-items:center;justify-content:center;letter-spacing:.2px}
.header-rule{left:50px;top:62px;width:568px;height:1px;background:var(--line)}
.main-nav{left:0;top:71px;width:668px;display:flex;justify-content:center;gap:16px;font-size:7.4px;font-weight:500;color:var(--ink)}
.main-nav .current{color:var(--accent)}

/* intro */
.intro-mark{left:320px;top:133px;width:28px;height:28px;border-radius:50%;background:var(--accent-soft)}
.page-title{left:0;top:158px;width:668px;text-align:center;font-family:"Playfair Display",serif;font-weight:700;font-size:28px;color:var(--ink)}
.intro-text{left:137px;top:194px;width:394px;text-align:center;font-size:8.8px;line-height:13px;color:var(--ink)}
.hero-photo{left:75px;top:275px;width:518px;height:274px;background:linear-gradient(90deg,#5f7a3f 0%,#a9a39a 35%,#c9cacb 60%,#b9b8b6 100%)}

/* help section */
.help-photo{left:50px;top:610px;width:265px;height:265px;border-radius:50%;background:radial-gradient(circle at 45% 50%,#f1d8ca 0%,#e7bfa8 60%,#d9a48c 100%);box-shadow:0 0 0 4px #f3e3dc}
.help-title{left:342px;top:622px;font-family:"Playfair Display",serif;font-weight:700;font-size:22px;color:var(--ink-dark);letter-spacing:.3px}
.help-rule{left:342px;top:650px;width:35px;height:2px;background:var(--accent)}
.help-list{left:340px;top:659px;width:285px;list-style:none;font-size:8.6px;line-height:13px;color:var(--ink)}
.help-list li{margin-bottom:5px}

/* footer */
.site-footer{left:0;top:935px;width:668px;height:265px;background:var(--footer);color:var(--footer-text)}
.footer-brand{left:60px;top:85px;width:175px;display:flex;flex-direction:column;align-items:center;gap:8px}
.footer-brand .brand-dot{width:48px;height:48px;background:#c9a3a8}
.footer-brand .brand-name{color:var(--white);font-size:15px}
.footer-heading{font-family:"Playfair Display",serif;font-weight:700;font-size:14px;color:var(--white)}
.useful-links{left:262px;top:66px}
.useful-links ul{list-style:none;margin-top:4px;font-size:8.2px;line-height:15px}
.contact{left:423px;top:66px}
.contact-row{display:flex;align-items:flex-start;gap:6px;font-size:8.2px;line-height:15px;margin-top:1px}
.contact-row svg{flex:none;margin-top:4px}
.contact-indent{padding-left:12px}
.social{display:flex;gap:3px;margin-top:8px}
.social span{width:15px;height:15px;border-radius:50%;background:#6a696c}
.footer-rule{left:50px;top:234px;width:568px;height:1px;background:var(--footer-line)}
.copyright{left:0;top:242px;width:668px;text-align:center;font-size:8.6px;color:var(--white)}
.to-top{left:625px;top:225px;width:19px;height:19px;border-radius:50%;background:var(--accent);display:flex;align-items:center;justify-content:center}
</style>
</head>
<body>

<header class="site-header">
  <div class="abs call-box">
    <svg width="8" height="8" viewBox="0 0 24 24"><path fill="#b0747c" d="M6.6 10.8a15 15 0 0 0 6.6 6.6l2.2-2.2c.3-.3.7-.4 1-.2 1.1.4 2.3.6 3.6.6.6 0 1 .4 1 1V20c0 .6-.4 1-1 1A17 17 0 0 1 3 4c0-.6.4-1 1-1h3.5c.6 0 1 .4 1 1 0 1.3.2 2.5.6 3.6.1.3 0 .7-.2 1z"/></svg>
  </div>
  <div class="abs call-text"><span class="call-label">CALL NOW</span><span class="call-number">413-555-0186</span></div>
  <div class="abs brand"><span class="brand-dot"></span><span class="brand-name">Willowgate Acupuncture</span></div>
  <div class="abs shop-button">ONLINE SHOP</div>
  <div class="abs header-rule"></div>
  <nav class="abs main-nav">
    <span>About</span><span>Fertility &amp; Pregnancy</span><span class="current">Hormone Balance</span><span>Strength &amp; Structure</span><span>Emotional wellbeing</span><span>Testimonials</span>
  </nav>
</header>

<main>
  <div class="abs intro-mark"></div>
  <h1 class="abs page-title">Hormone Balance</h1>
  <p class="abs intro-text">Our hormones are constantly shifting and occasionally this internal orchestra needs to be refined. Acupuncture works to help the body rediscover the positive patterns that lead to improved health and well being. By repeating these patterns we are reminding the body how to access greater health on its own.</p>
  <div class="abs hero-photo" role="img" aria-label="Overhead view of whole foods: leafy greens, beans, grains, vegetables, spices and pasta on a grey stone table"></div>

  <div class="abs help-photo" role="img" aria-label="Close-up of an acupuncture needle being placed during a treatment"></div>
  <h2 class="abs help-title">ACUPUNCTURE CAN HELP:</h2>
  <div class="abs help-rule"></div>
  <ul class="abs help-list">
    <li>Stop painful periods &nbsp;and manage fibroids, endometriosis and ovulatory pain</li>
    <li>Encourage regular menstrual cycles</li>
    <li>Regulate ovulation for PCOS</li>
    <li>Calm hormone imbalances that can lead to migraines</li>
    <li>Hyperthyroid /hypothyroid conditions</li>
    <li>Minimize the symptoms of menopause including hot flashes, night sweats, insomnia, vaginal</li>
    <li>Dryness, depression, brain fog and irritability help rebuild after adrenal fatigue/burnout</li>
    <li>Hormonal support and surgical recovery for gender affirmation help minimize side effects of hormonal birth control methods</li>
    <li>Help to manage PMDD</li>
  </ul>
</main>

<footer class="abs site-footer">
  <div class="abs footer-brand"><span class="brand-dot"></span><span class="brand-name">Willowgate Acupuncture</span></div>
  <div class="abs useful-links">
    <h3 class="footer-heading">Useful Links</h3>
    <ul>
      <li>About</li><li>Fertility &amp; Pregnancy (nest)</li><li>Hormone Balance (rocks)</li><li>Strength &amp; Structure (tree)</li><li>Emotional wellbeing (heart)</li><li>Online Shop</li><li>Testimonials</li>
    </ul>
  </div>
  <div class="abs contact">
    <h3 class="footer-heading">Contact Us</h3>
    <div class="contact-row" style="margin-top:4px">
      <svg width="6" height="8" viewBox="0 0 12 16"><path fill="#d9b3b7" d="M6 0a6 6 0 0 0-6 6c0 4.5 6 10 6 10s6-5.5 6-10a6 6 0 0 0-6-6zm0 8.2A2.2 2.2 0 1 1 6 3.8a2.2 2.2 0 0 1 0 4.4z"/></svg>
      <span>Contact Willowgate Acupuncture</span>
    </div>
    <div class="contact-row contact-indent">Easthollow MA14 Birchfield Lane</div>
    <div class="contact-row contact-indent">Easthollow, MA 01099</div>
    <div class="contact-row">
      <svg width="7" height="7" viewBox="0 0 24 24"><path fill="#d9b3b7" d="M6.6 10.8a15 15 0 0 0 6.6 6.6l2.2-2.2c.3-.3.7-.4 1-.2 1.1.4 2.3.6 3.6.6.6 0 1 .4 1 1V20c0 .6-.4 1-1 1A17 17 0 0 1 3 4c0-.6.4-1 1-1h3.5c.6 0 1 .4 1 1 0 1.3.2 2.5.6 3.6.1.3 0 .7-.2 1z"/></svg>
      <span>413-555-0186</span>
    </div>
    <div class="contact-row" style="margin-top:3px">
      <svg width="7" height="6" viewBox="0 0 16 12"><path fill="#d9b3b7" d="M0 0h16v1.5L8 7 0 1.5zM0 3.5l8 5.5 8-5.5V12H0z"/></svg>
      <span>hello@willowgateacupuncture.com</span>
    </div>
    <div class="social"><span></span><span></span><span></span><span></span></div>
  </div>
  <div class="abs footer-rule"></div>
  <div class="abs to-top">
    <svg width="6" height="4" viewBox="0 0 10 6"><path d="M1 5l4-4 4 4" fill="none" stroke="#fff" stroke-width="1.4"/></svg>
  </div>
  <p class="abs copyright">Copyright © 2020 Willowgate Acupuncture</p>
</footer>

</body>
</html>
```